Lord Barnaby's Shave & Grooming Products

Shave soap and balm label design
Lord Barnaby’s is a new brand by a business that produces gentlemen’s grooming products. Our first two products will be a shaving soap and a post shave balm. We require label designs for both. There may be additional products in the future within these categories, so it is important all text fields need to be editable. We have adopted the moose as a “mascot” and would like to incorporate that into the label in a creative way with some designer discretion. We desire the label to include a vintage/traditional/old school vibe with that will appeal to both the older and younger gentleman.
The winning designer will also have the opportunity to design future products and other designs i.e. stickers, t-shirts,
promotional material, etc. If you have any questions, feel free to ask. We look forward to seeing your designs.

Target Market(s)

Every man that shaves between the ages of 18 and 80

Industry/Entity Type

Hair And Beauty

Logo Text

Lord Barnaby's

Colors

Designer to choose colors to be used in the design.

Requirements
Must have
• SHAVE SOAP
• Our shave soap containers will be circular and need to accommodate a label sizeable from 88-100mm (exact size not finalized to date)
• SHAVE SOAP TOP LABEL REQUIREMENTS:
• TITLE Lord Barnaby’s
• SUB TITLE Fine Tallow Shave Soap
• ORIGIN St. Louis, Missouri – USA
• QUANTITY Net Wt. 4.0 oz’s
• SCENT Sandalwood
• URL www.lordbarnabysgoods.example
• SHAVE BALM
• Our balm container is circular and is 96mm across and 20mm tall. Label area 20mm X 300mm on the side.
• We would like a label for both the top and side of the jar. Balm label must have the following elements:
• TOP LABEL REQUIREMENTS:
• TITLE Lord Barnaby’s
• SUB TITLE Fine Post Shave Balm
• QUANTITY Net Wt. 3.0 oz’s
• SCENT Sandalwood
• SIDE LABEL REQUIREMENTS:
• TITLE Lord Barnaby’s
• ORIGIN (optional) St. Louis, Missouri – USA
• SCENT Sandalwood
• INGREDIENTS Aloe Barbadensis Leaf Juice, Witch Hazel Distillate, Vitis Vinifera
• Seed Oil, Polysorbate 60, Glycerin, Vitamin E Oil, Pure Essential
• Oils, Propylene Glycol, Diazolidinyl Urea, Methylparaben, and Propylparaben
• URL (optional) www.lordbarnabysgoods.example
• REQUIRED FILE FORMAT
•  Adobe Illustrator file with all vectors (not flattened)
•  all fields must be editable
Nice to have
• LOOK AND FEEL
•  Masculine
•  Bold
•  Serious
•  Traditional
•  Personable
•  Colorful
•  Value
Should not have
• Text "Fine Tallow Shave Soap" should not be more prominent than the brand name "Lord Barnaby's" See graphic below for sample.

```html
<!DOCTYPE html>
<html lang="en">
<head>
<meta charset="utf-8">
<title>Lord Barnaby's Label Set</title>
<link rel="stylesheet" href="https://fonts.googleapis.com/css2?family=Jost:wght@400;600&display=swap">
<style>
  :root {
    --ink: #111111;
    --gold: #d4a33a;
    --grey: #6e6e6e;
    --rule: #1a1a1a;
    --edge: #9a9a9a;
    --paper: #ffffff;
  }
  * { margin: 0; padding: 0; box-sizing: border-box; }
  html, body { width: 1200px; height: 580px; overflow: hidden; background: var(--paper); }
  body { position: relative; font-family: "Jost", Arial, sans-serif; color: var(--ink); }

  .top-label {
    position: absolute; width: 306px; height: 306px;
    border: 1px solid var(--edge); border-radius: 50%;
  }
  .top-label--balm { left: 22px; top: 22px; }
  .top-label--soap { left: 867px; top: 22px; }

  .jar-front { position: absolute; left: 382px; top: 10px; width: 224px; height: 320px; }

  .side-label {
    position: absolute; left: 23px; top: 378px; width: 1149px; height: 177px;
    border: 1px solid var(--edge);
  }

  .rule { position: absolute; height: 1.5px; background: var(--rule); }

  .mascot-mark {
    position: absolute; transform: translate(-50%, -50%);
    width: 36px; height: 36px; border-radius: 50%; background: var(--ink);
  }

  .brand {
    position: absolute; transform: translate(-50%, -50%);
    font-weight: 600; font-size: 20px; letter-spacing: 0.5px;
    white-space: nowrap; background: var(--paper); padding: 0 8px;
    color: var(--ink);
  }

  .centered { position: absolute; transform: translateX(-50%); text-align: center; white-space: nowrap; }
  .product-name { font-size: 11px; color: var(--gold); letter-spacing: 0.3px; }
  .scent { font-size: 10px; color: var(--grey); letter-spacing: 0.4px; }
  .origin { font-size: 5.5px; color: var(--grey); letter-spacing: 0.2px; }
  .origin--gold { color: var(--gold); }
  .url { font-size: 5.5px; color: var(--grey); }
  .net-weight { font-size: 6px; color: var(--ink); }
  .ingredients { font-size: 5.5px; line-height: 10.5px; color: var(--grey); }
</style>
</head>
<body>

  <section class="top-label top-label--balm">
    <div class="mascot-mark" role="img" aria-label="Moose mascot" style="left:153px; top:76px;"></div>
    <div class="brand" style="left:153px; top:112px;">LORD BARNABY’S</div>
    <div class="centered product-name" style="left:153px; top:161px;">FINE POST SHAVE BALM</div>
    <div class="centered scent" style="left:153px; top:176px;">SANDALWOOD</div>
    <div class="rule" style="left:74px; width:156px; top:208px;"></div>
    <div class="centered origin" style="left:153px; top:243px;">MADE IN ST LOUIS, MISSOURI, USA</div>
    <div class="centered url" style="left:153px; top:252px;">www.lordbarnabysgoods.example</div>
  </section>

  <section class="jar-front">
    <div class="mascot-mark" role="img" aria-label="Moose mascot" style="left:112px; top:150px;"></div>
    <div class="rule" style="left:0; width:224px; top:178px;"></div>
    <div class="brand" style="left:112px; top:186px;">LORD BARNABY’S</div>
    <div class="centered product-name" style="left:112px; top:230px;">FINE POST SHAVE BALM</div>
    <div class="centered scent" style="left:112px; top:245px;">SANDALWOOD</div>
    <div class="rule" style="left:0; width:224px; top:264px;"></div>
    <div class="centered net-weight" style="left:112px; top:289px;">Net Wt 3.0 oz</div>
  </section>

  <section class="top-label top-label--soap">
    <div class="mascot-mark" role="img" aria-label="Moose mascot" style="left:153px; top:76px;"></div>
    <div class="brand" style="left:153px; top:112px;">LORD BARNABY’S</div>
    <div class="centered product-name" style="left:153px; top:161px;">FINE TALLOW SHAVE SOAP</div>
    <div class="centered scent" style="left:153px; top:176px;">SANDALWOOD</div>
    <div class="rule" style="left:74px; width:156px; top:208px;"></div>
    <div class="centered origin" style="left:153px; top:243px;">MADE IN ST LOUIS, MISSOURI, USA</div>
    <div class="centered url" style="left:153px; top:252px;">www.lordbarnabysgoods.example</div>
  </section>

  <section class="side-label">
    <div class="mascot-mark" role="img" aria-label="Moose mascot" style="left:287px; top:32px;"></div>
    <div class="rule" style="left:0; right:0; top:65px;"></div>
    <div class="rule" style="left:0; right:0; top:150px;"></div>
    <div class="brand" style="left:287px; top:68px;">LORD BARNABY’S</div>
    <div class="centered product-name" style="left:287px; top:109px;">FINE POST SHAVE BALM</div>
    <div class="centered scent" style="left:287px; top:123px;">SANDALWOOD</div>
    <div class="centered net-weight" style="left:287px; top:158px;">Net Wt 3.0 oz</div>

    <div class="centered ingredients" style="left:858px; top:75px;">
      INGREDIENTS: Aloe Barbadensis Leaf Juice, Witch Hazel Distillate, Vitis Vinifera<br>
      Seed Oil, Polysorbate 60, Glycerin, Vitamin E Oil, Pure Essential Oils,<br>
      Propylene Glycol, Diazolidinyl Urea, Methylparaben, Propylparaben
    </div>
    <div class="centered origin origin--gold" style="left:858px; top:119px;">MADE IN ST. LOUIS, MISSOURI USA</div>
    <div class="centered url" style="left:858px; top:132px;">www.lordbarnabysgoods.example</div>
  </section>

</body>
</html>
```